A wine Label for a new brand of New Zealand Wine

We are looking for a Wine Label for our "Harbor Crest" brand of wines from North Otago New Zealand. We would like the label to perhaps use the HC as a logo and the rest up to the designer. We have our vineyards located in the Waitaki Valley New Zealand which is a southern region with mountains and a river flowing past our vineyard. Photos attached of Dramatic Landscape. Also attached is a basic outline of requirements for the front bottle of the label. The rear bottle label will contain writing about the wines background plus statutory regulations on Alc. Vol, bar code etc. Front Label size to be no Larger than 80mm deep by 100 mm wide. The label can be simple or graphic, whatever the designer chooses.
Target Market(s)
New Wine Brand
Look and feel
Each slider illustrates characteristics of the customer's brand and the style your logo design should communicate.

```html
<!DOCTYPE html>
<html lang="en">
<head>
<meta charset="utf-8">
<title>Harbor Crest – Pinot Gris 2015 Front Label</title>
<link rel="stylesheet" href="https://fonts.googleapis.com/css2?family=Cinzel:wght@600&family=Cormorant+SC:wght@500;600&family=Montserrat:wght@500&display=swap">
<style>
  :root {
    --canvas: #ffffff;
    --gold-bright: #e3cf1a;
    --gold-mid: #b9a214;
    --gold-deep: #6f6410;
    --olive: #4c4a12;
    --ink-light: #f2f0e6;
    --sky: #5b6a7a;
    --mountain: #4b5544;
    --vine: #3f5a2c;
    --vine-light: #7d8a52;
  }
  * { margin: 0; padding: 0; box-sizing: border-box; }
  html, body {
    width: 1200px;
    height: 1000px;
    overflow: hidden;
    background: var(--canvas);
  }
  .label {
    position: absolute;
    left: 335px;
    top: 168px;
    width: 530px;
    height: 663px;
    background: linear-gradient(180deg, #050505 0%, #141512 35%, #1f2428 44%);
    overflow: hidden;
  }
  .label__landscape {
    position: absolute;
    left: 0;
    top: 290px;
    width: 530px;
    height: 354px;
    background:
      linear-gradient(180deg,
        var(--sky) 0%,
        #6f7c84 9%,
        var(--mountain) 12%,
        #6b6a4a 20%,
        var(--vine) 28%,
        var(--vine-light) 48%,
        #55622f 70%,
        #2b2a12 100%);
  }
  .label__bottom-shade {
    position: absolute;
    left: 0;
    top: 570px;
    width: 530px;
    height: 74px;
    background: linear-gradient(180deg, rgba(0,0,0,0) 0%, rgba(20,18,4,0.85) 100%);
  }
  .band {
    position: absolute;
    left: 0;
    width: 530px;
  }
  .band--top {
    top: 0;
    height: 30px;
    background: linear-gradient(180deg, var(--gold-deep) 0%, var(--gold-bright) 45%, var(--gold-mid) 100%);
  }
  .band--top-shadow {
    top: 30px;
    height: 15px;
    background: linear-gradient(180deg, #2e2b08 0%, #3a370c 100%);
  }
  .band--top-olive {
    top: 45px;
    height: 22px;
    background: linear-gradient(180deg, var(--gold-deep) 0%, var(--olive) 100%);
  }
  .band--bottom {
    bottom: 0;
    height: 19px;
    background: linear-gradient(180deg, var(--gold-mid) 0%, var(--gold-bright) 50%, var(--gold-deep) 100%);
  }
  .shield {
    position: absolute;
    left: 0;
    top: 0;
    width: 530px;
    height: 663px;
  }
  .text {
    position: absolute;
    left: 86px;
    width: 357px;
    text-align: center;
  }
  .monogram {
    top: 124px;
    font-family: "Cinzel", serif;
    font-weight: 600;
    font-size: 50px;
    line-height: 56px;
    color: var(--gold-bright);
  }
  .brand {
    top: 212px;
    font-family: "Cinzel", serif;
    font-weight: 600;
    font-size: 64px;
    line-height: 68px;
    color: var(--gold-bright);
    letter-spacing: 1px;
  }
  .varietal {
    top: 430px;
    font-family: "Cormorant SC", serif;
    font-weight: 600;
    font-size: 34px;
    line-height: 36px;
    color: var(--ink-light);
  }
  .vintage {
    top: 466px;
    font-family: "Cormorant SC", serif;
    font-weight: 600;
    font-size: 27px;
    line-height: 30px;
    color: var(--ink-light);
  }
  .region {
    top: 518px;
    left: 76px;
    width: 377px;
    font-family: "Cormorant SC", serif;
    font-weight: 500;
    font-size: 21px;
    line-height: 26px;
    color: var(--ink-light);
  }
  .origin {
    top: 558px;
    font-family: "Montserrat", sans-serif;
    font-weight: 500;
    font-size: 15px;
    line-height: 20px;
    letter-spacing: 2.5px;
    color: var(--ink-light);
  }
</style>
</head>
<body>
  <main class="label" aria-label="Harbor Crest Pinot Gris front label">
    <div class="label__landscape" role="img" aria-label="Photograph of vineyard rows in the Waitaki Valley with mountains behind"></div>
    <div class="label__bottom-shade"></div>

    <div class="band band--top"></div>
    <div class="band band--top-shadow"></div>
    <div class="band band--top-olive"></div>
    <div class="band band--bottom"></div>

    <svg class="shield" viewBox="0 0 530 663" aria-hidden="true">
      <defs>
        <linearGradient id="shield-fill" x1="0" y1="0" x2="0" y2="1">
          <stop offset="0" stop-color="#000" stop-opacity="0.92"/>
          <stop offset="0.55" stop-color="#0a0a06" stop-opacity="0.6"/>
          <stop offset="1" stop-color="#000" stop-opacity="0.8"/>
        </linearGradient>
      </defs>
      <path d="M68 639 V150 Q68 86 150 80 H380 Q461 86 461 150 V639 Z"
            fill="rgba(120,100,10,0.35)" stroke="#8a7a12" stroke-opacity="0.55" stroke-width="4"/>
      <path d="M86 630 V160 Q86 104 156 100 H374 Q443 104 443 160 V630 Z"
            fill="url(#shield-fill)"/>
      <rect x="86" y="421" width="357" height="73" fill="#8c7c14" fill-opacity="0.7"/>
      <rect x="86" y="494" width="357" height="136" fill="#000" fill-opacity="0.72"/>
    </svg>

    <div class="text monogram">HC</div>
    <h1 class="text brand">HARBOR<br>CREST</h1>
    <p class="text varietal">Pinot Gris</p>
    <p class="text vintage">2015</p>
    <p class="text region">Waitaki Valley - North Ortago</p>
    <p class="text origin">NEW ZEALAND WINE</p>
  </main>
</body>
</html>
```